Professional and creatice Life Coach - Business Card design

I just relaunched my website and now i a need a correspoonding business card for my task as life coach. My website is www.tbalrond.com as reference. The compass is kind of a symbol for my work, as I help people navigate through their challenging phases in life. The business card should be colorful, but not too playful as I also adress business people. So it sould be creative, but professional (also to suport my other business as Management Consultant)

Target Market(s)

People who want to get teir problems resolved, in business, partnership and other personal realms

Industry/Entity Type

Life Coaching

Contact Information for Business Card

Front side should include Name, Phone number, Email, Website and address

Font styles to use
Sans Serif

Colors
add136

Requirements
Must have
• "Mag. Leopold Brantner" -> Name
"Energetische Praxis" -> Jobtitle (describing my profession as life coach)
colours and style should match my website www.tbalrond.com
Nice to have
• a compass as a symbol

```html
<!DOCTYPE html>
<html lang="de">
<head>
<meta charset="utf-8">
<title>Mag. Leopold Brantner – Visitenkarte</title>
<link rel="stylesheet" href="https://fonts.googleapis.com/css2?family=EB+Garamond:wght@600;700&family=Poppins:wght@400;600;700&display=swap">
<style>
  :root {
    --lime: #c6fb4d;
    --lime-bright: #a6ff00;
    --black: #0a0a0a;
    --forest: #2c4128;
    --ink: #1c1c1c;
    --icon: #2d3b2a;
    --white: #ffffff;
    --page: #ffffff;
  }
  * { box-sizing: border-box; margin: 0; padding: 0; }
  html, body { width: 848px; height: 1200px; overflow: hidden; background: var(--page); }
  .sheet { position: relative; width: 848px; height: 1200px; }

  .card {
    position: absolute; left: 59px; width: 714px; height: 429px;
    background: var(--lime); overflow: hidden;
  }
  .card--front { top: 72px; }
  .card--back { top: 603px; }
  .card__shapes { position: absolute; inset: 0; width: 714px; height: 429px; }

  .side-label {
    position: absolute; left: 0; width: 848px; text-align: center;
    font-family: "Poppins", sans-serif; font-weight: 700; font-size: 46px;
    color: var(--black); letter-spacing: 0.5px;
  }
  .side-label--front { top: 508px; left: -5px; }
  .side-label--back { top: 1040px; left: -12px; }

  .identity { position: absolute; left: 59px; top: 66px; }
  .identity__name {
    font-family: "EB Garamond", serif; font-weight: 700; font-size: 31px;
    font-variant: small-caps; letter-spacing: 0.6px; color: var(--ink); line-height: 1;
  }
  .identity__title {
    margin-top: 12px;
    font-family: "EB Garamond", serif; font-weight: 700; font-size: 20px;
    letter-spacing: 1.6px; color: var(--ink); line-height: 1;
  }

  .contact { position: absolute; left: 59px; top: 231px; list-style: none; }
  .contact__item {
    display: flex; align-items: center; height: 33px;
    font-family: "Poppins", sans-serif; font-size: 15.5px; color: var(--ink);
  }
  .contact__item:nth-child(2) { height: 32px; }
  .contact__item:nth-child(3) { height: 35px; }
  .contact__icon { width: 20px; height: 20px; margin-right: 24px; flex: none; }

  .emblem { position: absolute; left: 441px; top: 156px; width: 244px; height: 244px; }

  .photo-area { position: absolute; inset: 0; }

  .web-block {
    position: absolute; left: 0; top: 290px; width: 272px; text-align: center;
    font-family: "Poppins", sans-serif; font-size: 15.5px; color: var(--ink);
  }
  .web-block__icon { width: 18px; height: 18px; display: block; margin: 0 auto 10px; }
  .web-block strong { font-weight: 700; }
</style>
</head>
<body>
<main class="sheet">

  <section class="card card--front" aria-label="Vorderseite">
    <svg class="card__shapes" viewBox="0 0 714 429" aria-hidden="true">
      <polygon points="549,0 714,0 714,46 524,46" fill="var(--lime-bright)"/>
      <polygon points="0,0 549,0 528,36 0,36" fill="var(--black)"/>
      <polygon points="0,380 399,380 369,429 0,429" fill="var(--forest)"/>
      <line x1="296" y1="125" x2="714" y2="125" stroke="var(--black)" stroke-width="1.6"/>
      <circle cx="291" cy="125" r="7.5" fill="var(--white)" stroke="var(--black)" stroke-width="1.4"/>
    </svg>

    <header class="identity">
      <h1 class="identity__name">Mag. Leopold Brantner</h1>
      <p class="identity__title">Energetische Praxis</p>
    </header>

    <ul class="contact">
      <li class="contact__item">
        <svg class="contact__icon" viewBox="0 0 20 20" aria-hidden="true"><path d="M2 7c0-3 4-4 8-4s8 1 8 4v2h-4V7.5H6V9H2z M4 10h12l1 7H3z" fill="var(--icon)"/><circle cx="10" cy="13.5" r="2" fill="var(--lime)"/></svg>
        +43 660 4817392
      </li>
      <li class="contact__item">
        <svg class="contact__icon" viewBox="0 0 20 20" aria-hidden="true" fill="none" stroke="var(--icon)" stroke-width="1.2"><circle cx="10" cy="10" r="8"/><ellipse cx="10" cy="10" rx="3.6" ry="8"/><path d="M2 10h16M3.2 6h13.6M3.2 14h13.6"/></svg>
        www.tbalrond.com
      </li>
      <li class="contact__item">
        <svg class="contact__icon" viewBox="0 0 20 20" aria-hidden="true"><rect x="1" y="4" width="18" height="12" fill="var(--icon)"/><path d="M1.5 4.5 10 11l8.5-6.5M1.5 15.5l6-5.5M18.5 15.5l-6-5.5" fill="none" stroke="var(--lime)" stroke-width="1.2"/></svg>
        leopold@brantner.one
      </li>
      <li class="contact__item">
        <svg class="contact__icon" viewBox="0 0 20 20" aria-hidden="true"><path d="M10 1.5a5.5 5.5 0 0 0-5.5 5.5c0 4.2 5.5 11.5 5.5 11.5s5.5-7.3 5.5-11.5A5.5 5.5 0 0 0 10 1.5z" fill="var(--icon)"/><circle cx="10" cy="7" r="2.1" fill="var(--lime)"/></svg>
        Lindenweg 12, 5020 Salzburg, Austria
      </li>
    </ul>

    <svg class="emblem" viewBox="0 0 244 244" role="img" aria-label="Kompassrose als Symbol der Praxis">
      <defs>
        <radialGradient id="emblem-tone" cx="50%" cy="50%" r="50%">
          <stop offset="0" stop-color="#ffffff" stop-opacity="0.55"/>
          <stop offset="0.25" stop-color="#2a2a2a" stop-opacity="0.55"/>
          <stop offset="1" stop-color="#2a2a2a" stop-opacity="0"/>
        </radialGradient>
      </defs>
      <circle cx="122" cy="122" r="120" fill="url(#emblem-tone)"/>
    </svg>
  </section>

  <p class="side-label side-label--front">FRONT</p>

  <section class="card card--back" aria-label="Rückseite">
    <svg class="card__shapes" viewBox="0 0 714 429" aria-hidden="true">
      <defs>
        <linearGradient id="forest-tone" x1="0" y1="0" x2="0" y2="1">
          <stop offset="0" stop-color="#b9c6c9"/>
          <stop offset="0.25" stop-color="#5d7b4c"/>
          <stop offset="0.6" stop-color="#3f6a2c"/>
          <stop offset="1" stop-color="#2f4f24"/>
        </linearGradient>
      </defs>
      <polygon points="0,0 370,0 399,47 0,47" fill="var(--forest)"/>
      <polygon class="photo-area" points="129,47 713,47 713,391 278,391" fill="url(#forest-tone)" role="img" aria-label="Foto: Hand hält einen Kompass vor einem Bergwald"/>
      <polygon points="524,379 714,379 714,429 549,429" fill="var(--lime-bright)"/>
      <polygon points="0,391 530,391 549,429 0,429" fill="var(--black)"/>
      <line x1="0" y1="347" x2="262" y2="347" stroke="var(--black)" stroke-width="1.6"/>
      <circle cx="266" cy="347" r="7.5" fill="var(--white)" stroke="var(--black)" stroke-width="1.4"/>
    </svg>

    <div class="web-block">
      <svg class="web-block__icon" viewBox="0 0 20 20" aria-hidden="true" fill="none" stroke="var(--icon)" stroke-width="1.2"><circle cx="10" cy="10" r="8"/><ellipse cx="10" cy="10" rx="3.6" ry="8"/><path d="M2 10h16M3.2 6h13.6M3.2 14h13.6"/></svg>
      www.<strong>tbalrond</strong>.com
    </div>
  </section>

  <p class="side-label side-label--back">BACK</p>

</main>
</body>
</html>
```